The Varley's Wedding invitations

Looking for wedding invitations with at least 3 pictures of us on one side and one picture on the other side, Something romantic. Need 100 invitations 5x7 matte with envelopes. This is for a lesbian wedding. Want it to be catchy, modern yet romantic. I've given a few pictures. I trust you'll select the right ones for the project. I've enclosed some invitations I saw online. I do like the one wit 3 pics on one side, but our pics don't match the way theirs did.

Target Market(s)

Wedding guest

Font styles to use
Script

Colors

Designer to choose colors to be used in the design.

Requirements
Must have
• Marla & Tessa
• soon to be THE VARLEY'S (front side 3 pictures)
• Marlene Forbush & Tessa Varley (back side- 1 picture)
• HAPPILY INVITE YOU TO
• CELEBRATE
• THEIR WEDDING
• 09/30/2018 5pm at:
• Opal Lounge:
• 4816 Pelham Ave
• Riverside, Ca 92519
Should not have
• .

```html
<!DOCTYPE html>
<html lang="en">
<head>
<meta charset="utf-8">
<title>The Varley's Wedding Invitation</title>
<link href="https://fonts.googleapis.com/css2?family=Yesteryear&family=Bree+Serif&family=Cabin:wght@400;500&display=swap" rel="stylesheet">
<style>
  :root {
    --bg: #5a5a5a;
    --paper: #ffffff;
    --tan: #e2cc98;
    --tan-deep: #d9bf85;
    --brown: #7a5219;
    --ink: #3b2a14;
    --photo-warm: #a89a8c;
    --photo-cool: #7d8a8f;
    --photo-dark: #4a4440;
  }
  * { box-sizing: border-box; margin: 0; padding: 0; }
  html, body { width: 1200px; height: 1200px; overflow: hidden; }
  body {
    background: var(--bg);
    position: relative;
    font-family: "Cabin", sans-serif;
    color: var(--brown);
  }
  .card {
    position: absolute;
    top: 222px;
    width: 540px;
    height: 756px;
    box-shadow: 0 6px 18px rgba(0,0,0,.35);
    overflow: hidden;
  }
  .card--front { left: 40px; background: var(--paper); }
  .card--back { left: 620px; background: var(--tan); }

  /* front */
  .rule {
    position: absolute;
    left: 55px; width: 433px; height: 0;
    border-top: 2px dotted var(--brown);
  }
  .rule--top { top: 21px; }
  .rule--bottom { top: 108px; }
  .couple-title {
    position: absolute;
    top: 26px; left: 0; width: 100%;
    text-align: center;
    font-family: "Yesteryear", cursive;
    font-size: 54px;
    line-height: 1.3;
    color: var(--brown);
  }
  .couple-title .amp {
    font-family: "Cabin", sans-serif;
    font-size: 30px;
    margin: 0 22px;
    vertical-align: 8px;
  }
  .photo { position: absolute; }
  .photo--engaged { left: 37px; top: 123px; width: 239px; height: 398px;
    background: linear-gradient(160deg, var(--photo-cool), #d7d4cd 55%, #bdb6ae); }
  .photo--selfie { left: 286px; top: 123px; width: 223px; height: 341px;
    background: linear-gradient(170deg, var(--photo-dark), var(--photo-warm) 50%, #5b5e4c); }
  .photo--coast { left: 37px; top: 533px; width: 239px; height: 198px;
    background: linear-gradient(100deg, var(--photo-dark), #a08275 45%, #6f8fa8); }
  .soon-box {
    position: absolute;
    left: 286px; top: 477px; width: 223px; height: 254px;
    background: var(--tan);
    text-align: center;
  }
  .soon-box .rule { left: 16px; width: 191px; }
  .soon-box .rule--top { top: 12px; }
  .soon-box .rule--bottom { top: 240px; }
  .soon-label { position: absolute; top: 52px; width: 100%; font-size: 17px; color: var(--brown); }
  .soon-name {
    position: absolute; top: 86px; width: 100%;
    font-family: "Yesteryear", cursive; font-size: 46px; color: var(--brown);
  }
  .soon-name small { font-family: "Bree Serif", serif; font-size: 19px; vertical-align: 18px; margin-right: 2px; }
  .soon-date { position: absolute; top: 180px; width: 100%; font-size: 17px; color: var(--brown); }

  /* back */
  .photo--kiss { left: 0; top: 0; width: 540px; height: 400px;
    background: linear-gradient(180deg, #6f7a5e 0%, #8c7a6a 40%, #4a4a55 100%); }
  .lace-band { position: absolute; left: 0; top: 360px; width: 540px; height: 165px;
    background: linear-gradient(180deg, rgba(74,74,85,0) 0%, #c9b88e 35%, #dcc796 70%, var(--tan) 100%); }
  .names {
    position: absolute; top: 530px; left: 0; width: 100%;
    display: flex; justify-content: center; align-items: flex-start; gap: 18px;
  }
  .name { text-align: center; }
  .name__first {
    font-family: "Bree Serif", serif; font-size: 50px; line-height: 1; color: var(--brown);
  }
  .name__last {
    font-family: "Yesteryear", cursive; font-size: 25px; line-height: .8; color: var(--brown);
  }
  .names .amp { font-family: "Cabin", sans-serif; font-size: 34px; color: var(--ink); margin-top: 30px; }
  .invite-line {
    position: absolute; top: 626px; width: 100%; text-align: center;
    font-family: "Bree Serif", serif; font-size: 15px; color: var(--ink); letter-spacing: .2px;
  }
  .details {
    position: absolute; top: 664px; left: 0; width: 100%;
    display: flex; justify-content: center;
    font-family: "Bree Serif", serif; font-size: 15px; line-height: 1.38; color: var(--ink); text-align: center;
  }
  .details__col { width: 230px; }
  .details__divider { width: 0; height: 78px; border-left: 2px dotted var(--brown); margin-top: -2px; }
</style>
</head>
<body>
  <section class="card card--front">
    <div class="rule rule--top"></div>
    <h1 class="couple-title">Marla<span class="amp">&amp;</span>Tessa</h1>
    <div class="rule rule--bottom"></div>
    <div class="photo photo--engaged" role="img" aria-label="Photo of the couple holding up an 'I said yes' sign"></div>
    <div class="photo photo--selfie" role="img" aria-label="Close-up selfie of the couple"></div>
    <div class="photo photo--coast" role="img" aria-label="Selfie of the couple by the ocean"></div>
    <div class="soon-box">
      <div class="rule rule--top"></div>
      <p class="soon-label">Soon to be</p>
      <p class="soon-name"><small>The</small>Varley's</p>
      <p class="soon-date">09/30/18</p>
      <div class="rule rule--bottom"></div>
    </div>
  </section>

  <section class="card card--back">
    <div class="photo photo--kiss" role="img" aria-label="Photo of the couple sharing a kiss outdoors"></div>
    <div class="lace-band" role="img" aria-label="Gold lace border"></div>
    <div class="names">
      <div class="name">
        <div class="name__first">MARLENE</div>
        <div class="name__last">Forbush</div>
      </div>
      <span class="amp">&amp;</span>
      <div class="name">
        <div class="name__first">TESSA</div>
        <div class="name__last">Varley</div>
      </div>
    </div>
    <p class="invite-line">HAPPILY INVITE YOU TO CELEBRATE THEIR WEDDING</p>
    <div class="details">
      <div class="details__col">SUNDAY<br>September 30, 2018<br>5 PM</div>
      <div class="details__divider"></div>
      <div class="details__col">OPAL LOUNGE<br>4816 Pelham Ave,<br>Riverside, Ca 92519</div>
    </div>
  </section>
</body>
</html>
```